SkyvoraQ Business Cards and Stationary Design

Need a design for our business cards and stationary. I want to carry on the theme of the logo. I want the business cards to have a design on the back. I would like the business cards and the stationary to carry the same theme, design scheme, and branding

Target Market(s)

Airlines and Maintenance Facilities

Industry/Entity Type

Aviation

Contact Information for Business Card

Name
Position Title
Address: 4827 Tollbeck Lane, Fort Pierce, Florida, 34951
Office Number
Mobile Number
Email
Website

Font styles to use
Serif
Sans Serif

Colors

Designer to choose colors to be used in the design.

```html
<!DOCTYPE html>
<html lang="en">
<head>
<meta charset="utf-8">
<title>SkyvoraQ Business Card</title>
<link rel="stylesheet" href="https://fonts.googleapis.com/css2?family=Cinzel:wght@600&family=Montserrat:wght@700&family=Arimo:wght@400&display=swap">
<style>
  :root {
    --page-bg: #e6e2dc;
    --card-white: #f3f3f2;
    --card-lower: #ecebea;
    --navy: #1b2d5a;
    --navy-deep: #13224a;
    --blue: #1f5fa8;
    --ink: #1c2233;
    --text: #26282c;
    --rule: #c9c9cb;
  }
  html, body {
    margin: 0;
    padding: 0;
    width: 1200px;
    height: 970px;
    overflow: hidden;
    background: var(--page-bg);
  }
  .canvas {
    position: relative;
    width: 1200px;
    height: 970px;
  }
  .card {
    position: absolute;
    left: 68px;
    top: 190px;
    width: 1064px;
    height: 590px;
    border-radius: 30px;
    overflow: hidden;
    box-shadow: 0 10px 30px rgba(0,0,0,0.18);
  }
  .card-shapes {
    position: absolute;
    inset: 0;
  }
  .wordmark {
    position: absolute;
    left: 0;
    right: 0;
    top: 240px;
    margin: 0;
    text-align: center;
    font-family: "Montserrat", sans-serif;
    font-weight: 700;
    font-size: 54px;
    letter-spacing: 11px;
    color: var(--ink);
    line-height: 1;
  }
  .contact-list {
    position: absolute;
    left: 136px;
    top: 376px;
    margin: 0;
    padding: 0;
    list-style: none;
    font-family: "Arimo", sans-serif;
    font-size: 26px;
    color: var(--text);
  }
  .contact-item {
    display: flex;
    align-items: center;
    height: 35.8px;
  }
  .contact-icon {
    width: 24px;
    height: 24px;
    margin-right: 12px;
    flex: none;
  }
  .holder {
    position: absolute;
    right: 124px;
    top: 368px;
    text-align: right;
  }
  .holder-name {
    margin: 0;
    font-family: "Cinzel", serif;
    font-weight: 600;
    font-size: 40px;
    color: var(--blue);
    line-height: 1.1;
  }
  .holder-title {
    margin: 0;
    font-family: "Arimo", sans-serif;
    font-size: 27px;
    color: var(--text);
    line-height: 1.2;
  }
</style>
</head>
<body>
<div class="canvas">
  <div class="card">
    <svg class="card-shapes" width="1064" height="590" viewBox="0 0 1064 590">
      <defs>
        <linearGradient id="topBand" x1="0" y1="0" x2="0" y2="1">
          <stop offset="0" stop-color="#e9e9ea"/>
          <stop offset="1" stop-color="#8f9096"/>
        </linearGradient>
        <linearGradient id="sideBlue" x1="0" y1="0" x2="0" y2="1">
          <stop offset="0" stop-color="#2a4376"/>
          <stop offset="1" stop-color="#0f1d45"/>
        </linearGradient>
        <linearGradient id="lowerShade" x1="0" y1="0" x2="0" y2="1">
          <stop offset="0" stop-color="#d4d4d6"/>
          <stop offset="0.1" stop-color="#ecebea"/>
          <stop offset="1" stop-color="#e8e7e6"/>
        </linearGradient>
      </defs>
      <rect class="upper-panel" x="0" y="0" width="1064" height="318" fill="var(--card-white)"/>
      <rect class="top-band" x="0" y="0" width="1064" height="45" fill="url(#topBand)"/>
      <path class="top-corner" d="M0 0 H22 V45 H0 Z" fill="var(--navy)"/>
      <path class="top-corner" d="M1042 0 H1064 V45 H1042 Z" fill="var(--navy)"/>
      <rect class="lower-panel" x="0" y="318" width="1064" height="272" fill="url(#lowerShade)"/>
      <path class="side-band-left" d="M0 318 H68 L107 590 H0 Z" fill="url(#sideBlue)"/>
      <path class="side-band-right" d="M1000 318 H1064 V590 H967 Z" fill="url(#sideBlue)"/>
      <line x1="68" y1="318" x2="1000" y2="318" stroke="var(--rule)" stroke-width="2"/>
    </svg>

    <p class="wordmark">SKYVORAQ</p>

    <ul class="contact-list">
      <li class="contact-item">
        <svg class="contact-icon" viewBox="0 0 24 24" aria-hidden="true"><rect width="24" height="24" rx="3" fill="var(--navy)"/><rect x="8" y="4" width="8" height="16" rx="1.5" fill="none" stroke="#fff" stroke-width="1.8"/></svg>
        +01 555 410 382
      </li>
      <li class="contact-item">
        <svg class="contact-icon" viewBox="0 0 24 24" aria-hidden="true"><rect width="24" height="24" rx="3" fill="var(--navy)"/><path d="M8 5 L10.5 8.5 L9 10 Q10.5 13.5 14 15 L15.5 13.5 L19 16 L17.5 19 Q10 19 5.5 10 Z" fill="#fff"/></svg>
        +01 555 410 382
      </li>
      <li class="contact-item">
        <svg class="contact-icon" viewBox="0 0 24 24" aria-hidden="true"><rect width="24" height="24" rx="3" fill="var(--navy)"/><rect x="5" y="7" width="14" height="10" fill="none" stroke="#fff" stroke-width="1.6"/><path d="M5 7 L12 13 L19 7" fill="none" stroke="#fff" stroke-width="1.6"/></svg>
        info@skyvoraq.com
      </li>
      <li class="contact-item">
        <svg class="contact-icon" viewBox="0 0 24 24" aria-hidden="true"><rect width="24" height="24" rx="3" fill="var(--navy)"/><circle cx="12" cy="12" r="7" fill="none" stroke="#fff" stroke-width="1.6"/><path d="M5 12 H19 M12 5 Q8 12 12 19 M12 5 Q16 12 12 19" fill="none" stroke="#fff" stroke-width="1.3"/></svg>
        www.skyvoraq.com
      </li>
      <li class="contact-item">
        <svg class="contact-icon" viewBox="0 0 24 24" aria-hidden="true"><rect width="24" height="24" rx="3" fill="var(--navy)"/><path d="M12 20 Q6 13 6 10 A6 6 0 0 1 18 10 Q18 13 12 20 Z" fill="#fff"/><circle cx="12" cy="10" r="2.3" fill="var(--navy)"/></svg>
        4827 Tollbeck Lane, Fort Pierce, Florida, 34951
      </li>
    </ul>

    <div class="holder">
      <p class="holder-name">MARA HOLT</p>
      <p class="holder-title">Position</p>
    </div>
  </div>
</div>
</body>
</html>
```